Website Design for a holiday home letting busines

We require a redesign of our present website www.birchwoodstays.com. We want the website to stand out and look professional and clean to make holiday hunters want to book a caravan or lodge holiday with us. Our logo is red however we DO NOT want the website to be red. We want a natural colour scheme.

The final design should communicate that we are a professional company to book with.

On the home page we require;
Overview of company
Photo
Search box for holiday (check in)
Late Deals
Reviews
News

We would like the following pages designed; home page, available dates page, caravans page, content page.

The website should be responsive for smart phones. One website I do like is http://www.verdamoro.be/nl/

Target Market(s)

Families

Industry/Entity Type

Travel

Number of Pages Required

5+ page

Font styles to use
Serif

Requirements
Must have
• The project must be responsive for mobile phones and tablets.
• Ability to search for holiday home holidays
• We want a natural colour scheme.
Nice to have
• A style we like is http://www.verdamoro.be/nl/
Should not have
• Do not use red as a colour for the website. Our logo is red so this is the only time we want this used.

```html
<!DOCTYPE html>
<html lang="en">
<head>
<meta charset="utf-8">
<title>Birchwood Stays – Lodge &amp; Caravan Holidays</title>
<link href="https://fonts.googleapis.com/css2?family=Open+Sans:wght@400;600;700;800&display=swap" rel="stylesheet">
<style>
:root{
  --blue:#2d5d9f;
  --blue-dark:#234a80;
  --navy:#1e2a3a;
  --navy-deep:#151e2a;
  --green:#5a9b35;
  --green-dark:#467d27;
  --red:#c8242b;
  --text:#333b44;
  --muted:#6b7480;
  --light:#eef1f4;
  --line:#d7dce2;
  --white:#ffffff;
}
*{box-sizing:border-box;margin:0;padding:0}
html,body{width:1200px;height:2400px;overflow:hidden}
body{font-family:"Open Sans",Arial,sans-serif;color:var(--text);background:var(--white);font-size:13px;line-height:1.45}
a{color:inherit;text-decoration:none}

/* header */
.site-header{height:48px;display:flex;align-items:center;justify-content:space-between;padding:0 40px}
.brand{display:flex;align-items:center;gap:10px;color:var(--red);font-weight:700;font-size:24px}
.brand-square{width:22px;height:22px;background:var(--red)}
.header-contact{display:flex;align-items:center;gap:18px;font-size:12px;color:var(--muted)}
.header-contact p{display:flex;align-items:center;gap:6px;line-height:1.6}
.header-contact strong{color:var(--blue)}
.chat-btn{background:var(--red);color:var(--white);font-weight:700;padding:7px 14px;border-radius:4px;font-size:14px}

.main-nav{height:32px;background:var(--blue);display:flex;padding:0 40px}
.main-nav a{color:var(--white);font-size:12px;font-weight:600;padding:0 14px;line-height:32px}
.main-nav a.active{background:var(--blue-dark)}

/* hero */
.hero{position:relative;height:520px;background:linear-gradient(180deg,#b9d2e6 0%,#8fb07a 35%,#5f8a45 70%,#4a6f35 100%)}
.promo{position:absolute;right:40px;top:30px;width:330px;text-align:right}
.promo h1{background:var(--blue);color:var(--white);font-size:26px;font-weight:800;padding:12px 18px;text-align:left}
.promo p{color:var(--white);font-weight:700;font-size:16px;margin:10px 0;text-shadow:0 1px 3px rgba(0,0,0,.6);text-align:left}
.promo .btn{display:inline-block;float:left}
.btn{background:var(--blue);color:var(--white);font-weight:700;font-size:12px;padding:7px 16px;border-radius:3px}
.search{position:absolute;left:40px;bottom:20px;width:760px}
.search-tabs{display:flex}
.search-tabs span{background:var(--blue);color:var(--white);font-weight:700;font-size:14px;padding:6px 22px}
.search-tabs span+span{background:var(--navy);}
.search-form{background:rgba(30,42,58,.88);padding:12px;display:grid;grid-template-columns:repeat(3,1fr) 170px;gap:8px}
.field{background:var(--white);height:26px;font-size:11px;color:var(--muted);padding:0 8px;display:flex;align-items:center;justify-content:space-between}
.field::after{content:"▾";color:var(--text)}
.check-btn{background:var(--green);color:var(--white);font-weight:700;grid-row:span 2;display:flex;align-items:center;justify-content:center;font-size:13px}
.signup{position:absolute;right:40px;bottom:20px;width:330px;background:rgba(255,255,255,.94)}
.signup h2{background:var(--blue);color:var(--white);font-size:14px;font-weight:800;padding:8px 12px}
.signup-body{padding:12px;display:flex;flex-direction:column;gap:8px}
.input{border:1px solid var(--line);height:26px;font-size:11px;color:var(--muted);padding:0 8px;display:flex;align-items:center;background:var(--white)}
.signup .btn{align-self:flex-start;font-size:11px;padding:5px 12px}

/* intro */
.intro{height:270px;padding:26px 190px 0;text-align:center}
.intro h2{font-size:22px;font-weight:800;color:var(--navy)}
.intro .lead{font-size:12px;color:var(--muted);margin:4px 0 10px}
.intro h3{font-size:18px;font-weight:800;color:var(--navy);margin-bottom:8px}
.intro p{font-size:11.5px;color:var(--text);margin-bottom:8px}

/* caravans */
.caravans{height:460px;background:linear-gradient(180deg,#6f8f4e,#4f7236 60%,#3f5e2c);padding-top:26px}
.section-banner{display:block;width:max-content;margin:0 auto;background:var(--green);color:var(--white);font-size:20px;font-weight:800;padding:8px 28px}
.caravan-grid{display:flex;justify-content:center;gap:24px;margin-top:26px}
.caravan-card{width:290px;background:var(--white);box-shadow:0 3px 10px rgba(0,0,0,.3)}
.photo{background:linear-gradient(180deg,#c8d8e4,#98b383 55%,#6e8e54)}
.caravan-card .photo{height:160px}
.caravan-info{padding:12px 14px}
.caravan-info h3{font-size:15px;font-weight:800;color:var(--navy);margin-bottom:6px}
.specs{display:grid;grid-template-columns:1fr 1fr;font-size:11px;color:var(--muted);gap:2px 10px;margin-bottom:12px}
.specs b{color:var(--text);font-weight:600}
.card-actions{display:flex;gap:8px}
.card-actions a{flex:1;text-align:center;color:var(--white);font-weight:700;font-size:12px;padding:6px 0}
.btn-green{background:var(--green)}
.btn-blue{background:var(--blue)}

/* late deals */
.late-deals{height:290px;background:var(--light);padding-top:24px}
.title-rule{display:flex;align-items:center;justify-content:center;gap:18px;font-size:20px;font-weight:800;color:var(--navy)}
.title-rule::before,.title-rule::after{content:"";width:70px;height:2px;background:var(--blue)}
.deal-grid{display:flex;justify-content:center;gap:20px;margin-top:18px}
.deal-card{width:250px;background:var(--white);border:1px solid var(--line)}
.deal-card .photo{height:100px;position:relative;background:linear-gradient(180deg,#cfdde8,#e9edf0 50%,#a9bf93)}
.price{position:absolute;right:0;bottom:8px;background:var(--green);color:var(--white);font-weight:800;font-size:15px;padding:3px 12px}
.deal-info{padding:8px 10px;font-size:11px;color:var(--muted)}
.deal-info h3{font-size:13px;font-weight:800;color:var(--navy)}
.deal-info .date{color:var(--text);font-weight:600}
.deal-info .meta{display:flex;gap:14px;margin-top:3px}
.book{display:block;background:var(--blue);color:var(--white);text-align:center;font-weight:700;font-size:12px;padding:6px 0}

/* feeds */
.feeds{height:570px;display:grid;grid-template-columns:1fr 1fr 1fr;gap:36px;padding:26px 40px 0}
.feed h2{font-size:17px;font-weight:800;color:var(--navy);border-bottom:2px solid var(--blue);padding-bottom:6px;margin-bottom:14px}
.post{display:flex;gap:12px;margin-bottom:18px}
.post .photo{width:100px;height:70px;flex:none}
.post p{font-size:11.5px;color:var(--text)}
.post time{display:block;font-size:11px;color:var(--muted);margin-top:4px}
.review{border-bottom:1px solid var(--line);padding-bottom:12px;margin-bottom:12px}
.review-head{display:flex;justify-content:space-between;align-items:center}
.review-head b{color:var(--blue);font-size:13px}
.stars{color:#e0a21b;font-size:13px;letter-spacing:1px}
.review p{font-size:11.5px;margin:4px 0}
.review small{font-size:11px;color:var(--muted)}
.social-box{border:1px solid var(--line);padding:12px}
.social-top{display:flex;gap:10px;align-items:center;border-bottom:1px solid var(--line);padding-bottom:10px}
.social-top .sq{width:46px;height:46px;background:var(--green)}
.social-top b{font-size:13px;color:var(--navy);display:block}
.social-top span{font-size:11px;color:var(--muted)}
.like{margin-left:auto;background:var(--blue);color:var(--white);font-size:11px;font-weight:700;padding:3px 10px}
.social-box .count{font-size:11px;color:var(--muted);margin:10px 0 8px}
.avatar-grid{display:grid;grid-template-columns:repeat(5,1fr);gap:8px}
.avatar-grid span{height:56px;background:linear-gradient(135deg,#b7c7a4,#7e9a68)}
.avatar-grid span:nth-child(3n){background:linear-gradient(135deg,#c7d3de,#8ca4bb)}
.avatar-grid span:nth-child(4n){background:linear-gradient(135deg,#dccdb2,#b39d78)}

/* footer */
.site-footer{height:210px;background:var(--navy);color:#c9d1db}
.footer-cols{display:grid;grid-template-columns:1.2fr 1fr 1fr;gap:40px;padding:22px 40px 0;height:172px}
.site-footer h2{color:var(--white);font-size:14px;font-weight:700;margin-bottom:10px}
.links{display:grid;grid-template-columns:1fr 1fr;font-size:11.5px;gap:3px 10px}
.links a::before{content:"› ";color:var(--green)}
.contact p{font-size:11.5px;line-height:1.6}
.video{height:110px;background:linear-gradient(135deg,#3c5a78,#6d8aa5);display:flex;align-items:center;justify-content:center}
.footer-bar{height:38px;background:var(--navy-deep);display:flex;align-items:center;justify-content:space-between;padding:0 40px;font-size:11px}
.cards{display:flex;gap:6px}
.cards span{width:34px;height:22px;background:#4b5b70}
</style>
</head>
<body>

<header class="site-header">
  <a class="brand" href="#"><span class="brand-square"></span>Birchwood Stays</a>
  <div class="header-contact">
    <div>
      <p><svg width="12" height="12" viewBox="0 0 24 24"><path fill="#2d5d9f" d="M6.6 10.8a15 15 0 0 0 6.6 6.6l2.2-2.2c.3-.3.7-.4 1-.2 1.1.4 2.3.6 3.6.6.6 0 1 .4 1 1V20c0 .6-.4 1-1 1A17 17 0 0 1 3 4c0-.6.4-1 1-1h3.5c.6 0 1 .4 1 1 0 1.3.2 2.5.6 3.6.1.3 0 .7-.2 1z"/></svg>Call us: <strong>01632 960 418</strong></p>
      <p><svg width="12" height="12" viewBox="0 0 24 24"><path fill="#2d5d9f" d="M2 5h20v14H2zm2 2v.5l8 5 8-5V7l-8 5z"/></svg>Email us: <strong>info@birchwoodstays.com</strong></p>
    </div>
    <a class="chat-btn" href="#">Chat Now</a>
  </div>
</header>

<nav class="main-nav">
  <a class="active" href="#">Home</a><a href="#">News</a><a href="#">Reviews</a><a href="#">Caravans &amp; Lodges</a><a href="#">2015 Holidays</a><a href="#">2016 Holidays</a><a href="#">Payment Plans</a><a href="#">Kestrel Bay</a><a href="#">Local Attractions</a><a href="#">Contact Us</a>
</nav>

<section class="hero" role="img" aria-label="Family relaxing at a picnic table outside a static caravan on a sunny holiday park lawn">
  <div class="promo">
    <h1>PRIVATE HOLIDAY RENTALS</h1>
    <p>QUALITY LODGE &amp; CARAVAN HIRE AT KESTREL BAY HOLIDAY PARK. BOOK ONLINE TODAY!</p>
    <a class="btn" href="#">BOOK DETAILS</a>
  </div>
  <div class="search">
    <div class="search-tabs"><span>2015 Holidays</span><span>2016 Holidays</span></div>
    <div class="search-form">
      <span class="field">Caravan type</span>
      <span class="field">Grade</span>
      <span class="field">Nights</span>
      <a class="check-btn" href="#">Check availability</a>
      <span class="field">Bedrooms</span>
      <span class="field">Sleeps</span>
      <span class="field">Arrival date</span>
    </div>
  </div>
  <div class="signup">
    <h2>SIGN UP FOR OUR EMAIL</h2>
    <div class="signup-body">
      <span class="input">Your email address</span>
      <a class="btn" href="#">Subscribe</a>
    </div>
  </div>
</section>

<section class="intro">
  <h2>NO DEPOSIT HOLIDAYS</h2>
  <p class="lead">Would you like to book a 2016 caravan or lodge holiday at Kestrel Bay Holiday Park</p>
  <h3>PAY NO DEPOSIT?</h3>
  <p>We have flexible low cost weekly and monthly payment plans available. Spread the cost of your break over the months before you arrive, with no deposit to pay up front and no added fees.</p>
  <p>Once you select the dates that suit you, payments start within 28 days. You then have the chance to choose what day of the week or month your payment is taken, so your holiday is fully paid before you check in and your keys are ready.</p>
  <p>If you have any questions about our hassle free direct debit payment plans please contact us and we will be more than happy to help.</p>
</section>

<section class="caravans" role="img" aria-label="Holiday park grounds with caravans and lawns as a backdrop">
  <h2 class="section-banner">OUR CARAVANS AND LODGES</h2>
  <div class="caravan-grid">
    <article class="caravan-card">
      <div class="photo" role="img" aria-label="Exterior of the Fernhill caravan"></div>
      <div class="caravan-info">
        <h3>THE FERNHILL</h3>
        <div class="specs"><span>Caravan type: <b>Caravan</b></span><span>Grade: <b>Gold</b></span><span>Sleeps: <b>6</b></span><span>Bedrooms: <b>3</b></span></div>
        <div class="card-actions"><a class="btn-green" href="#">View details ›</a><a class="btn-blue" href="#">View Prices ›</a></div>
      </div>
    </article>
    <article class="caravan-card">
      <div class="photo" role="img" aria-label="Exterior of the Ashcombe lodge"></div>
      <div class="caravan-info">
        <h3>THE ASHCOMBE</h3>
        <div class="specs"><span>Caravan type: <b>Lodge</b></span><span>Grade: <b>Platinum</b></span><span>Sleeps: <b>6</b></span><span>Bedrooms: <b>3</b></span></div>
        <div class="card-actions"><a class="btn-green" href="#">View details ›</a><a class="btn-blue" href="#">View Prices ›</a></div>
      </div>
    </article>
    <article class="caravan-card">
      <div class="photo" role="img" aria-label="Exterior of the Larkspur caravan"></div>
      <div class="caravan-info">
        <h3>THE LARKSPUR</h3>
        <div class="specs"><span>Caravan type: <b>Caravan</b></span><span>Grade: <b>Gold</b></span><span>Sleeps: <b>8</b></span><span>Bedrooms: <b>3</b></span></div>
        <div class="card-actions"><a class="btn-green" href="#">View details ›</a><a class="btn-blue" href="#">View Prices ›</a></div>
      </div>
    </article>
  </div>
</section>

<section class="late-deals">
  <h2 class="title-rule">LATE DEALS</h2>
  <div class="deal-grid">
    <article class="deal-card">
      <div class="photo" role="img" aria-label="Static caravan exterior"><span class="price">£275.00</span></div>
      <div class="deal-info"><h3>THE LARKSPUR</h3><p class="date">Friday 04 September 2015 (3 nights)</p><p class="meta"><span>Sleeps: 8</span><span>Bedrooms: 3</span></p></div>
      <a class="book" href="#">BOOK NOW</a>
    </article>
    <article class="deal-card">
      <div class="photo" role="img" aria-label="Static caravan exterior"><span class="price">£275.00</span></div>
      <div class="deal-info"><h3>THE LARKSPUR</h3><p class="date">Friday 11 September 2015 (3 nights)</p><p class="meta"><span>Sleeps: 8</span><span>Bedrooms: 3</span></p></div>
      <a class="book" href="#">BOOK NOW</a>
    </article>
    <article class="deal-card">
      <div class="photo" role="img" aria-label="Static caravan exterior"><span class="price">£275.00</span></div>
      <div class="deal-info"><h3>THE ASHCOMBE</h3><p class="date">Friday 18 September 2015 (3 nights)</p><p class="meta"><span>Sleeps: 6</span><span>Bedrooms: 3</span></p></div>
      <a class="book" href="#">BOOK NOW</a>
    </article>
    <article class="deal-card">
      <div class="photo" role="img" aria-label="Static caravan exterior"><span class="price">£275.00</span></div>
      <div class="deal-info"><h3>THE ROWAN II</h3><p class="date">Friday 25 September 2015 (3 nights)</p><p class="meta"><span>Sleeps: 6</span><span>Bedrooms: 2</span></p></div>
      <a class="book" href="#">BOOK NOW</a>
    </article>
  </div>
</section>

<section class="feeds">
  <div class="feed">
    <h2>Blog Feed</h2>
    <div class="post"><div class="photo" role="img" aria-label="Holiday park news photo"></div><p>New season dates are now open, book your summer caravan break early and save on peak weeks.<time>24 Aug 2015</time></p></div>
    <div class="post"><div class="photo" role="img" aria-label="Holiday park news photo"></div><p>Our newest lodge has arrived on site, with a hot tub deck and views across the lake.<time>18 Aug 2015</time></p></div>
    <div class="post"><div class="photo" role="img" aria-label="Holiday park news photo"></div><p>Family fun days are back this autumn with crafts, games and evening shows for all ages.<time>10 Aug 2015</time></p></div>
    <div class="post"><div class="photo" role="img" aria-label="Holiday park news photo"></div><p>Top walks and beaches within a short drive of the park, perfect for a relaxed day out.<time>02 Aug 2015</time></p></div>
  </div>
  <div class="feed">
    <h2>Latest reviews</h2>
    <div class="review"><div class="review-head"><b>Helen Marsh</b><span class="stars">★★★★★</span></div><p>Very clean on arrival, the caravan had everything we needed and the kids loved the pool. Friendly owners who could not do enough for us.</p><small>Stayed in: The Larkspur</small></div>
    <div class="review"><div class="review-head"><b>Claire Dunmore</b><span class="stars">★★★★★</span></div><p>Very enjoyable, spacious and modern lodge. Great location on the park and easy booking. Would happily stay again next year.</p><small>Stayed in: The Ashcombe</small></div>
    <div class="review"><div class="review-head"><b>Janet Pryce</b><span class="stars">★★★★☆</span></div><p>Me and my daughter and grandchildren had a great week. Lovely decking area and plenty of room, well worth the price.</p><small>Stayed in: The Rowan II</small></div>
  </div>
  <div class="feed">
    <h2>Community Feed</h2>
    <div class="social-box">
      <div class="social-top"><span class="sq"></span><div><b>Birchwood Stays</b><span>Holiday homes at Kestrel Bay</span></div><span class="like">Follow</span></div>
      <p class="count">1,248 people follow Birchwood Stays</p>
      <div class="avatar-grid"><span></span><span></span><span></span><span></span><span></span><span></span><span></span><span></span><span></span><span></span><span></span><span></span><span></span><span></span><span></span></div>
    </div>
  </div>
</section>

<footer class="site-footer">
  <div class="footer-cols">
    <div>
      <h2>Quick Links</h2>
      <div class="links"><a href="#">About us</a><a href="#">Kestrel Bay</a><a href="#">News</a><a href="#">Local Attractions</a><a href="#">Caravans &amp; Lodges</a><a href="#">Special Offers</a><a href="#">2015 Holidays</a><a href="#">Contact us</a><a href="#">2016 Holidays</a><a href="#">Terms &amp; Conditions</a><a href="#">Late Deals</a><a href="#">Privacy Policy</a></div>
    </div>
    <div class="contact">
      <h2>Contact Information</h2>
      <p>Birchwood Stays Ltd</p>
      <p>Unit 4, Millbrook Court, Harrowdale, HD7 2QX</p>
      <p>Tel: 01632 960 418</p>
      <p>info@birchwoodstays.com</p>
    </div>
    <div>
      <h2>View Video</h2>
      <div class="video" role="img" aria-label="Video preview of the holiday park"><svg width="40" height="40" viewBox="0 0 40 40"><circle cx="20" cy="20" r="19" fill="rgba(255,255,255,.85)"/><path d="M16 12l12 8-12 8z" fill="#1e2a3a"/></svg></div>
    </div>
  </div>
  <div class="footer-bar">
    <span>© 2015 Birchwood Stays Ltd. All Rights Reserved.</span>
    <div class="cards"><span></span><span></span><span></span><span></span></div>
  </div>
</footer>

</body>
</html>
```